Criação de Folder para Logística, Entrega & Armazenamento
" Na grande maioria dos meus negocio, hoje estamos com foco na venda de Gesso Agrícola, Calcário e milho. fazemos negócios com Produtores rurais e granjas. vendemos o gesso e entregamos com a nossa frota de caminhões seja, frota própria ou caminhões agregado. da mesma maneira são os negócios com grãos, originamos os grãos dos produtores e vedemos para as granjas, entregamos com a nossa frota própria ou caminhões agregados. "

```html
<!DOCTYPE html>
<html lang="pt-BR">
<head>
<meta charset="utf-8">
<title>Folder – Logística, Entrega &amp; Armazenamento</title>
<link rel="stylesheet" href="https://fonts.googleapis.com/css2?family=Oswald:wght@600;700&family=Open+Sans:wght@400;600&display=swap">
<style>
  :root{
    --page:#ececec;
    --orange:#ee8419;
    --orange-deep:#d86d0c;
    --peach:#f7d2a8;
    --cream:#f6ecdc;
    --mint:#e6efd6;
    --ink:#2a2a2a;
    --ink-soft:#3a3a3a;
    --white:#ffffff;
    --text:#4a3a2a;
  }
  *{box-sizing:border-box;margin:0;padding:0}
  html,body{width:1200px;height:1200px;overflow:hidden;background:var(--page)}
  body{font-family:"Open Sans",Arial,sans-serif;display:flex;align-items:center;justify-content:center}

  .folder{width:1120px;height:740px;display:grid;grid-template-columns:repeat(4,280px);box-shadow:0 14px 30px rgba(0,0,0,.18);background:var(--white)}
  .panel{position:relative;display:flex;flex-direction:column;overflow:hidden;border-right:1px solid rgba(0,0,0,.08)}
  .panel:last-child{border-right:none}

  .body-text{font-size:12px;line-height:1.55;color:var(--text);padding:14px 20px}
  .on-dark{color:#eaeaea}

  .section-title{font-family:"Oswald",Arial,sans-serif;font-weight:700;text-transform:uppercase;letter-spacing:.5px}

  /* Panel 1 — missão e visão */
  .panel--mission{background:linear-gradient(180deg,var(--orange) 0%,#f29a45 45%,var(--peach) 100%)}
  .panel--mission .top-strip{height:26px;background:var(--ink)}
  .label-box{display:inline-block;background:var(--ink);color:var(--white);font-family:"Oswald",Arial,sans-serif;font-weight:700;font-size:24px;line-height:1.05;padding:8px 14px;border-radius:4px;margin:26px 20px 0;text-transform:uppercase}
  .panel--mission .body-text{color:var(--white)}
  .wheat-mark{margin-top:auto;height:230px;background:linear-gradient(160deg,rgba(255,255,255,0) 0%,rgba(222,140,60,.35) 60%,rgba(200,120,40,.25) 100%)}

  /* Photo areas */
  .photo{position:relative;width:100%}
  .photo--harvest{height:230px;background:linear-gradient(180deg,#cfd6d8 0%,#d9c27a 45%,#b98d2f 100%)}
  .photo--grain{height:230px;background:linear-gradient(160deg,#e0b25a 0%,#b97a2b 55%,#7d4d1a 100%)}
  .photo--tractor{height:170px;background:linear-gradient(180deg,#d7cfc4 0%,#b69a7c 55%,#8a6648 100%)}
  .photo--field{height:170px;background:linear-gradient(180deg,#e2a640 0%,#c57f22 60%,#7e4e1b 100%)}
  .photo--sacks{height:170px;background:linear-gradient(135deg,#efe3c9 0%,#d6bd8c 50%,#b49262 100%)}

  .photo-title{position:absolute;left:18px;bottom:14px;font-size:30px;color:var(--white);text-shadow:0 2px 4px rgba(0,0,0,.45)}

  .band-light{background:var(--cream)}
  .band-mint{background:var(--mint)}
  .band-dark{background:var(--ink-soft);flex:1}
  .band-orange{background:var(--orange-deep)}
  .band-orange .body-text{color:var(--white)}
  .caption{background:var(--peach);flex:1}

  /* Panel 4 */
  .title-bar{background:linear-gradient(90deg,#6b3c14,#a35a1c);padding:10px 18px}
  .title-bar .section-title{font-size:28px;color:var(--white)}
  .panel--products .fill{flex:1;background:linear-gradient(180deg,#fbe6cf 0%,var(--peach) 100%);position:relative}
  .panel--products .wheat-mark{position:absolute;right:0;bottom:0;width:170px;height:220px;background:linear-gradient(200deg,rgba(255,255,255,0),rgba(214,130,50,.35))}
</style>
</head>
<body>
  <main class="folder">
    <section class="panel panel--mission">
      <div class="top-strip"></div>
      <div><h2 class="label-box">Nossa<br>Missão</h2></div>
      <p class="body-text">Comprar, transportar e entregar insumos e grãos com segurança, prazo e respeito ao produtor rural.</p>
      <div><h2 class="label-box">Nossa<br>Visão</h2></div>
      <p class="body-text">Ser referência regional em logística agrícola, ligando campo e granja com frota própria e agregada.</p>
      <div class="wheat-mark" role="img" aria-label="Ramos de trigo decorativos em tons de laranja"></div>
    </section>

    <section class="panel panel--company">
      <div class="photo photo--harvest" role="img" aria-label="Colheitadeira descarregando grãos em um campo de trigo">
        <h2 class="section-title photo-title">Empresa</h2>
      </div>
      <p class="body-text band-light">Atuamos na venda de gesso agrícola, calcário e milho para produtores rurais e granjas da região.</p>
      <div class="band-dark">
        <p class="body-text on-dark">Entregamos cada carga com nossa frota própria ou caminhões agregados, do campo ao destino final.</p>
      </div>
      <div class="photo photo--field" role="img" aria-label="Colheitadeira trabalhando na lavoura ao pôr do sol"></div>
      <p class="body-text caption">Armazenamento e controle de estoque para garantir entrega no tempo certo.</p>
    </section>

    <section class="panel panel--grains">
      <div class="photo photo--grain" role="img" aria-label="Mãos segurando grãos de milho colhidos">
        <h2 class="section-title photo-title">Nossos Grãos</h2>
      </div>
      <p class="body-text band-mint">Originamos os grãos direto dos produtores e vendemos para as granjas com total rastreabilidade.</p>
      <div class="band-dark">
        <p class="body-text on-dark">Milho selecionado, armazenado com cuidado e entregue por nossa frota em todo o estado.</p>
      </div>
      <div class="photo photo--sacks" role="img" aria-label="Sacos abertos com diferentes grãos e sementes"></div>
      <p class="body-text caption">Qualidade conferida em cada lote, da lavoura ao silo.</p>
    </section>

    <section class="panel panel--products">
      <div class="photo photo--tractor" role="img" aria-label="Trator aplicando corretivo no solo em área aberta"></div>
      <div class="title-bar"><h2 class="section-title">Nossos Adubos</h2></div>
      <p class="body-text band-mint">Gesso agrícola e calcário para corrigir o solo e aumentar a produtividade da sua lavoura.</p>
      <div class="band-orange">
        <p class="body-text">Venda com entrega direta na propriedade, em caminhões próprios ou agregados, conforme sua necessidade.</p>
      </div>
      <div class="fill">
        <div class="wheat-mark" role="img" aria-label="Espigas de trigo decorativas em tom laranja suave"></div>
      </div>
    </section>
  </main>
</body>
</html>
```